custom carpentry, woodworking and home repair company needs logo design and business card design

Attention: I apologize but I just received notification from my state that I cannot use the company name that I originally submitted (Beyond The Bench). The new name will be Lumbrella We need a company logo and business card design for our new company based in the Hampton Roads area of Virginia. The company name is Lumbrella. The final design should give a first impression of true craftsmanship and attention to detail. We would like the card to include the company name, my name Derek Halloway (owner), phone number (757) 482-3175, website (lumbrella-shop.example) and email address (derek@lumbrella-shop.example). Everything else is up to your discretion. Thanks, have fun, and good luck.

Industry/Entity Type

Business

Contact Information for Business Card

See project description

Logo Text

see project description

Colors

Designer to choose colors to be used in the design.

```html
<!DOCTYPE html>
<html lang="en">
<head>
<meta charset="utf-8">
<title>Lumbrella Business Card</title>
<link rel="stylesheet" href="https://fonts.googleapis.com/css2?family=Roboto+Slab:wght@300;400;600&display=swap">
<style>
  :root {
    --page: #ffffff;
    --card-shadow: rgba(40, 40, 50, 0.45);
    --wood-light: #b9a88c;
    --wood-mid: #9c8463;
    --wood-dark: #6f6250;
    --cream: #efeadf;
    --ink-grey: #6b6b6d;
    --text-grey: #7a7a7a;
    --band-tan: #d3c3a6;
    --band-deep: #bfae90;
    --key-tint: rgba(255, 255, 255, 0.35);
    --white: #ffffff;
  }
  * { margin: 0; padding: 0; box-sizing: border-box; }
  html, body {
    width: 1073px; height: 1200px; overflow: hidden;
    background: var(--page);
    font-family: "Roboto Slab", Georgia, serif;
  }
  .canvas { position: relative; width: 1073px; height: 1200px; }

  .card { position: absolute; overflow: hidden; }

  /* Front */
  .card-front {
    left: 45px; top: 37px; width: 931px; height: 532px;
    box-shadow: 14px 14px 22px var(--card-shadow);
  }
  .front-wood {
    position: absolute; inset: 0;
    background:
      linear-gradient(90deg, transparent 0 11%, rgba(40,35,30,.55) 11% 11.6%, transparent 11.6% 66%, rgba(40,35,30,.55) 66% 66.5%, transparent 66.5%),
      linear-gradient(100deg, var(--wood-dark) 0%, var(--wood-light) 30%, var(--wood-mid) 55%, var(--wood-light) 80%, var(--wood-mid) 100%);
  }
  .front-wordmark {
    position: absolute; left: 150px; top: 282px;
    font-size: 132px; font-weight: 600; line-height: 1;
    color: var(--white); letter-spacing: 2px;
  }
  .front-tagline {
    position: absolute; left: 303px; top: 472px;
    font-size: 23px; font-weight: 400; color: var(--white);
    text-shadow: 1px 1px 3px rgba(0,0,0,.75); white-space: nowrap;
  }

  /* Back */
  .card-back {
    left: 54px; top: 584px; width: 929px; height: 531px;
    background: var(--cream);
  }
  .back-wordmark {
    position: absolute; left: 64px; top: 170px;
    font-size: 78px; font-weight: 600; line-height: 1;
    color: var(--ink-grey);
  }
  .contact {
    position: absolute; right: 56px; top: 50px;
    text-align: right; color: var(--text-grey);
  }
  .contact-name { font-size: 30px; font-weight: 400; letter-spacing: .5px; line-height: 1.1; }
  .contact-role { font-size: 23px; font-weight: 300; margin-top: 2px; }
  .contact-phone { font-size: 29px; font-weight: 300; margin-top: 52px; }
  .contact-email { font-size: 25px; font-weight: 600; margin-top: 10px; }

  .key-strip {
    position: absolute; left: 32px; right: 32px; top: 323px; height: 58px;
    background: linear-gradient(90deg, var(--key-tint), rgba(255,255,255,.15), var(--key-tint));
  }
  .bottom-band {
    position: absolute; left: 0; right: 0; top: 350px; bottom: 0;
    background: radial-gradient(ellipse at 50% 45%, var(--band-deep) 0%, var(--band-tan) 60%);
  }
  .band-text {
    position: absolute; left: 0; right: 0; top: 405px;
    text-align: center; color: var(--white);
    text-shadow: 1px 1px 3px rgba(0,0,0,.55);
  }
  .band-site { font-size: 31px; font-weight: 600; line-height: 1.2; }
  .band-tagline { font-size: 23px; font-weight: 400; margin-top: 8px; }
</style>
</head>
<body>
<div class="canvas">
  <section class="card card-front">
    <div class="front-wood" role="img" aria-label="Weathered wooden plank background photograph"></div>
    <div class="front-wordmark">Lumbrella</div>
    <div class="front-tagline">custom carpentry • woodworking • home repairs</div>
  </section>

  <section class="card card-back">
    <div class="back-wordmark">Lumbrella</div>
    <div class="contact">
      <div class="contact-name">DEREK HALLOWAY</div>
      <div class="contact-role">owner</div>
      <div class="contact-phone">(757) 482-3175</div>
      <div class="contact-email">derek@lumbrella-shop.example</div>
    </div>
    <div class="bottom-band" role="img" aria-label="Faded photograph of a hand plane on a workbench"></div>
    <div class="key-strip" role="img" aria-label="Row of butterfly joinery keys"></div>
    <div class="band-text">
      <div class="band-site">lumbrella-shop.example</div>
      <div class="band-tagline">custom carpentry • woodworking • home repairs</div>
    </div>
  </section>
</div>
</body>
</html>
```